Creative Brief
Investment Banking Company Stationary
Business card, Letterhead, Envelope, Fax Cover
Professional
Daniyar Ospanturov
Managing Partner
27B Zheltoksan St,
Almaty, 050118
Kazakhstan
dospanturov@mailvero.kz
www.veltrafin.kz
The name of the company is Veltra Finance, LLP. In addition to the logo there should be text that includes the official name of the company.
I will need business cards for 3 other employees as well. Please message me for their relevant info.
Logo or blank

```html
<!DOCTYPE html>
<html lang="en">
<head>
<meta charset="utf-8">
<title>Veltra Finance, LLP — Stationery</title>
<link rel="stylesheet" href="https://fonts.googleapis.com/css2?family=Arimo:wght@400;700&display=swap">
<style>
:root{
  --stage:#6c6c6c;
  --navy:#34466d;
  --paper:#ffffff;
  --ink:#2d3a57;
  --grey-text:#555b66;
  --faint:#dfe2e8;
  --faint-text:#d6dae2;
}
*{box-sizing:border-box;margin:0;padding:0}
html,body{width:1200px;height:685px;overflow:hidden;background:var(--stage)}
body{position:relative;font-family:"Arimo",Arial,sans-serif;color:var(--grey-text)}
.sheet{position:absolute;background:var(--paper);overflow:hidden;box-shadow:0 1px 3px rgba(0,0,0,.35)}
.sheet svg.bg,.envelope-flap svg.bg{position:absolute;inset:0;width:100%;height:100%}

/* company name with a plain square beside it */
.brand{position:absolute;display:flex;align-items:center;justify-content:center;gap:6px}
.brand-square{display:block;background:var(--navy);flex:none}
.brand-name{font-family:"Arimo",Arial,sans-serif;font-weight:700;color:var(--ink);white-space:nowrap}
.brand.on-navy .brand-square{background:var(--paper)}
.brand.on-navy .brand-name{color:var(--paper)}
.watermark{position:absolute;font-family:"Arimo",Arial,sans-serif;font-weight:700;color:var(--faint-text);white-space:nowrap}

/* letterhead */
.letterhead{left:257px;top:24px;width:336px;height:629px}
.letterhead .contact-top{position:absolute;right:14px;top:9px;text-align:right;color:#fff;font-size:5px;line-height:1.5}
.letterhead .footer{position:absolute;left:0;right:0;bottom:14px;text-align:center;font-size:5px;line-height:1.6}

/* business cards */
.card-front{left:24px;top:199px;width:204px;height:112px}
.card-back{left:24px;top:312px;width:204px;height:112px}
.card-back .person{position:absolute;right:10px;top:12px;color:#fff;font-size:6px;line-height:1.4}
.card-back .person strong{font-weight:700}
.card-back .details{position:absolute;left:8px;top:62px;font-size:5px;line-height:1.5}

/* envelope */
.envelope-flap{position:absolute;left:629px;top:300px;width:509px;height:84px}
.envelope{left:629px;top:384px;width:509px;height:228px}
.envelope .return{position:absolute;left:10px;bottom:20px;font-size:5px;line-height:1.6}
</style>
</head>
<body>

<!-- Business card: front -->
<div class="sheet card-front">
  <svg class="bg" viewBox="0 0 204 112" preserveAspectRatio="none" aria-hidden="true">
    <rect width="204" height="112" fill="var(--navy)"/>
    <path d="M0 84 Q102 62 204 76 L204 112 L0 112 Z" fill="var(--paper)"/>
    <path d="M0 90 Q102 70 204 84" fill="none" stroke="var(--faint)" stroke-width="1.5"/>
  </svg>
  <div class="brand on-navy" style="right:12px;top:26px">
    <span class="brand-square" style="width:8px;height:8px"></span>
    <span class="brand-name" style="font-size:11px">Veltra Finance</span>
  </div>
</div>

<!-- Business card: back -->
<div class="sheet card-back">
  <svg class="bg" viewBox="0 0 204 112" preserveAspectRatio="none" aria-hidden="true">
    <path d="M0 0 L204 0 L204 52 Q120 44 60 56 Q30 62 0 58 Z" fill="var(--navy)"/>
    <path d="M0 62 Q40 66 100 56 Q160 46 204 56" fill="none" stroke="var(--faint)" stroke-width="1.5"/>
  </svg>
  <div class="brand on-navy" style="left:8px;top:26px">
    <span class="brand-name" style="font-size:13px">Veltra Finance</span>
  </div>
  <div class="person"><strong>Daniyar Ospanturov</strong><br>Managing Partner</div>
  <div class="details">
    27B Zheltoksan St, Almaty, 050118 Kazakhstan<br>
    Ph: +7 (727) 300-4120<br>
    Cell: +7 (701) 555 2043<br>
    Fax: +7 (727) 300-4121<br>
    dospanturov@mailvero.kz<br>
    www.veltrafin.kz
  </div>
</div>

<!-- Letterhead -->
<div class="sheet letterhead">
  <svg class="bg" viewBox="0 0 336 629" preserveAspectRatio="none" aria-hidden="true">
    <rect width="336" height="140" fill="var(--navy)"/>
    <path d="M0 140 L0 134 Q168 -40 336 134 L336 140 Z" fill="var(--paper)"/>
  </svg>
  <div class="contact-top">dospanturov@mailvero.kz<br>www.veltrafin.kz</div>
  <div class="brand" style="left:0;right:0;top:64px">
    <span class="brand-square" style="width:10px;height:10px"></span>
    <span class="brand-name" style="font-size:15px">Veltra Finance</span>
  </div>
  <div class="watermark" style="left:0;right:0;top:330px;text-align:center;font-size:36px">Veltra Finance</div>
  <div class="footer">
    27B Zheltoksan St, Almaty, 050118 Kazakhstan<br>
    Ph: +7 (727) 300-4120 &nbsp;Cell: +7 (701) 555 2043 &nbsp;Fax: +7 (727) 300-4121
  </div>
</div>

<!-- Envelope flap -->
<div class="envelope-flap">
  <svg class="bg" viewBox="0 0 509 84" preserveAspectRatio="none" aria-hidden="true">
    <path d="M0 84 L0 36 Q254 -22 509 36 L509 84 Z" fill="var(--navy)"/>
    <path d="M0 56 Q254 32 509 56 L509 70 Q254 48 0 72 Z" fill="var(--paper)"/>
  </svg>
  <div class="brand on-navy" style="left:0;right:0;top:14px">
    <span class="brand-square" style="width:7px;height:7px"></span>
    <span class="brand-name" style="font-size:10px">Veltra Finance</span>
  </div>
</div>

<!-- Envelope body -->
<div class="sheet envelope">
  <svg class="bg" viewBox="0 0 509 228" preserveAspectRatio="none" aria-hidden="true">
    <rect width="509" height="62" fill="var(--navy)"/>
    <path d="M0 62 L0 58 Q254 -2 509 58 L509 62 Z" fill="var(--paper)"/>
  </svg>
  <div class="brand" style="left:0;right:0;top:46px">
    <span class="brand-square" style="width:9px;height:9px"></span>
    <span class="brand-name" style="font-size:13px">Veltra Finance</span>
  </div>
  <div class="watermark" style="right:14px;top:142px;font-size:24px">Veltra Finance</div>
  <div class="return">
    27B Zheltoksan St, Almaty, 050118 Kazakhstan<br>
    Ph: +7 (727) 300-4120 Cell: +7 (701) 555 2043 Fax: +7 (727) 300-4121<br>
    Email: dospanturov@mailvero.kz &nbsp;Web: www.veltrafin.kz
  </div>
</div>

</body>
</html>
```